Logo+Business Card Design for Architecture Photographer

Hi Everyone,

I am looking for logo/business designs for my new business - Brovald Studio. My business does commercial photography with a specialization in architecture, luxury real estate, and design. The Int is short for interior and ex is short for exterior.

Some of the values of my business are:
- providing top quality photography and post-processing (straight lines, accurate and bold whites/blacks/colors) for commercial use (websites, social media, advertising campaigns)
- fostering a collaborative workflow that is professional and fun that will have clients returning because of the premium service they received
- asking the right questions so that I can capture what matters to my clients with my own creative vision

I want my final look to be modern and bold. The business cards will be letter pressed/debossed, so the design should incorporate that. I am imagining a solid matte olive green or matte navy blue background on one side and white on the other. The card will be printed on colored cards, so you don't have to put a colored background as part of the design. I have attached some examples of colors I like, although it doesn't matter too much for the purpose of your work.

I want the debossing to be part of the design of the business card. This debossing should be some some of pattern or a frame that holds the logo on the back of the card (I have attached some sample images named geometric debossing to show what I mean). Then I can just foil print my logo on the back. My contact info and a logo will be on the front.

Somewhere it should say "Architecture, Luxury Real Estate, Design".

My vision for the logo: no cameras or buildings. I can't think of anything symbolic for the logo, but it should somehow contain Brovald. It might be cool to have them separated by a line like Bro | Vald. Or have the Int inside something, and the Ex outside.

I plan on using Quelmark to print the cards. You can find their specifications here: https://quelmark.example/products/duplex-business-cards?variant=4837201956372

It would be nice to have a psd file that I can edit as well as a PDF to deliver to the printing company. Both must be vector graphics.

Thank you to everyone who has submitted a design as it has helped me get a better idea of what I want.

Target Market(s)

Designers, architects

Industry/Entity Type

Photographer

Contact Information for Business Card

See project description

Logo Text

Brovald Studio

Font styles to use
Sans Serif
Decorative

Colors
ffffff

Requirements
Must have
• Logo and business card design. Deboss area less than 3 square inches. Deboss area should be some sort of a pattern/design as shown in attachments labelled "Geometric Debossing Example".
• Logo design and deboss design must be submitted in vector graphics.
Nice to have
• Color doesn't have to be shown on the design because I will be printing on colored paper, although it would be helpful to help me visualize what it will eventually look like.
Should not have
• A camera or building in the design...too cliche.

```html
<!DOCTYPE html>
<html lang="en">
<head>
<meta charset="utf-8">
<title>Brovald Studio – Business Cards</title>
<link rel="stylesheet" href="https://fonts.googleapis.com/css2?family=Work+Sans:wght@400;600&display=swap">
<style>
  :root {
    --backdrop: #17181b;
    --card-navy: #2c2b78;
    --foil-gold: #c9a24a;
    --edge-gold: #b8862f;
  }
  * { margin: 0; padding: 0; box-sizing: border-box; }
  html, body {
    width: 1200px;
    height: 784px;
    overflow: hidden;
    background: var(--backdrop);
    font-family: "Work Sans", Arial, sans-serif;
  }
  .canvas {
    position: relative;
    width: 1200px;
    height: 784px;
  }
  .card {
    position: absolute;
    top: 243px;
    width: 520px;
    height: 298px;
    background: var(--card-navy);
    border-bottom: 3px solid var(--edge-gold);
    border-left: 2px solid var(--edge-gold);
    color: var(--foil-gold);
  }
  .card--front { left: 60px; }
  .card--back { left: 620px; }

  .wordmark {
    font-family: "Work Sans", Arial, sans-serif;
    font-weight: 600;
    color: var(--foil-gold);
    letter-spacing: 0.06em;
    line-height: 1;
  }

  /* Front: logo + contact details */
  .card--front .wordmark {
    position: absolute;
    left: 44px;
    top: 130px;
    font-size: 40px;
  }
  .divider {
    position: absolute;
    left: 262px;
    top: 70px;
    width: 1.5px;
    height: 158px;
    background: var(--foil-gold);
  }
  .contact {
    position: absolute;
    left: 288px;
    top: 74px;
    font-size: 11.5px;
    line-height: 1.5;
  }
  .contact__name {
    font-weight: 600;
    font-size: 17px;
    letter-spacing: 0.04em;
    text-transform: uppercase;
    line-height: 1.1;
  }
  .contact__title { margin-bottom: 12px; }
  .contact__address { margin-bottom: 10px; }
  .contact__line {
    display: flex;
    align-items: center;
    gap: 8px;
  }
  .contact__line svg {
    width: 10px;
    height: 10px;
    flex: none;
  }

  /* Back: centred logo */
  .card--back .wordmark {
    position: absolute;
    left: 0;
    right: 0;
    top: 118px;
    text-align: center;
    font-size: 60px;
  }
</style>
</head>
<body>
<main class="canvas">

  <section class="card card--front" aria-label="Business card front">
    <div class="wordmark">Brovald</div>
    <div class="divider"></div>
    <div class="contact">
      <p class="contact__name">Tobin Harwell</p>
      <p class="contact__title">Founder</p>
      <p class="contact__address">418 Larkmoor Avenue #207<br>Fenwick, OR 97431</p>
      <p class="contact__line">
        <svg viewBox="0 0 10 10" aria-hidden="true"><path d="M2 0.5 L3.6 0.5 L4.2 2.8 L3 3.6 Q4 6 6.4 7 L7.2 5.8 L9.5 6.4 L9.5 8 Q9.5 9.5 8 9.5 Q0.5 9 0.5 2 Q0.5 0.5 2 0.5 Z" fill="currentColor"/></svg>
        555-304-7186
      </p>
      <p class="contact__line">
        <svg viewBox="0 0 10 10" aria-hidden="true"><rect x="0.7" y="2" width="8.6" height="6" fill="none" stroke="currentColor" stroke-width="1"/><path d="M0.7 2 L5 5.4 L9.3 2" fill="none" stroke="currentColor" stroke-width="1"/></svg>
        info@brovaldstudio.example
      </p>
      <p class="contact__line">
        <svg viewBox="0 0 10 10" aria-hidden="true"><circle cx="5" cy="5" r="4.3" fill="none" stroke="currentColor" stroke-width="0.9"/><ellipse cx="5" cy="5" rx="1.9" ry="4.3" fill="none" stroke="currentColor" stroke-width="0.8"/><path d="M0.7 5 H9.3" stroke="currentColor" stroke-width="0.8"/></svg>
        www.brovaldstudio.example
      </p>
    </div>
  </section>

  <section class="card card--back" aria-label="Business card back">
    <div class="wordmark">Brovald</div>
  </section>

</main>
</body>
</html>
```